Retail/Wholesale website graphic template

I need to design a new graphic template for a website for a client. The website will be a retail/wholesale company site with most pages dedicated to presentation. There will also be an online store and a blog. However, you don't need to worry about those. All I need from you is a graphic template for a generic site page.

It will need to include standard UI elements, in case I need those. I am attaching a more detailed assignment in .docx format.

The logo is also attached.

Target Market(s)

small business owners, (occasional) retail customers

Industry/Entity Type

Wholesale

Number of Pages Required

1 page

Font styles to use
Serif
Sans Serif

Colors
ec1f27
474747

Requirements
Must have
• must match logo, be clean, minimal and with slightly larger text size
Should not have
• must not be modern-looking where you have to scroll and scroll and scroll to get to the bottom of the homepage. most of my visitors are "old" people, they do not get this type of design.

```html
<!DOCTYPE html>
<html lang="en">
<head>
<meta charset="utf-8">
<title>Corvan Traders — Home</title>
<link href="https://fonts.googleapis.com/css2?family=Jost:wght@300;400;500;600&family=Arimo:wght@400;700&display=swap" rel="stylesheet">
<style>
:root{
  --red:#ec1f27;
  --charcoal:#474747;
  --ink:#222;
  --text:#555;
  --muted:#888;
  --line:#d9d9d9;
  --band:#eceef1;
  --panel:#f3f3f3;
  --white:#fff;
}
*{box-sizing:border-box;margin:0;padding:0}
html,body{width:1200px;height:3390px;overflow:hidden;background:var(--white)}
body{font-family:"Arimo",Arial,sans-serif;color:var(--text);position:relative}
.wrap{width:1000px;margin:0 auto;position:relative}
h2.section-title{font-family:"Jost",sans-serif;font-weight:400;font-size:36px;color:var(--ink);text-align:center}
.btn{display:inline-block;background:var(--red);color:var(--white);font-family:"Jost",sans-serif;font-size:18px;padding:7px 18px;border-radius:2px}

/* header */
.site-header{height:100px}
.site-header .wrap{display:flex;justify-content:space-between;align-items:center;height:100px}
.brand{font-family:"Jost",sans-serif;font-weight:600;font-size:34px;color:var(--red);letter-spacing:1px;display:flex;align-items:center;gap:12px}
.brand .mark{width:22px;height:22px;background:var(--charcoal)}
.contact{display:flex;gap:34px;font-size:18px;color:var(--charcoal);align-items:center}
.contact span{display:flex;align-items:center;gap:10px}

/* nav */
.main-nav{height:38px;background:var(--charcoal);position:relative}
.main-nav a{position:absolute;top:9px;color:var(--white);font-family:"Jost",sans-serif;font-size:16px}
.main-nav a.active{color:var(--red)}

/* hero */
.hero{height:520px;position:relative;background:linear-gradient(180deg,#8a98a8 0%,#c9b79a 35%,#e9a85a 55%,#7d6a58 75%,#3e4b55 100%)}
.hero .arrow{position:absolute;top:247px;width:30px;height:30px;background:#2b2b2b;display:flex;align-items:center;justify-content:center}
.hero .arrow.prev{left:8px}.hero .arrow.next{right:8px}
.hero-caption{position:absolute;left:0;right:0;bottom:0;height:66px;background:rgba(0,0,0,.35);color:var(--white);font-family:"Jost",sans-serif;font-weight:600;font-size:31px;text-align:center;line-height:66px}

/* intro */
.intro{height:382px;padding-top:56px}
.intro .wrap{display:flex;justify-content:space-between}
.intro-text{width:640px}
.intro-text h1{font-family:"Jost",sans-serif;font-weight:400;font-size:36px;color:var(--ink);margin-bottom:20px}
.intro-text .lead{font-weight:700;font-size:14px;color:var(--ink);line-height:1.6;margin-bottom:14px}
.intro-text p{font-size:13.5px;line-height:1.75}
.advantages{width:326px;height:270px;background:var(--panel);border:1px solid #e3e3e3}
.advantages header{height:42px;background:var(--charcoal);display:flex;align-items:center;padding:0 12px;gap:14px;font-family:"Jost",sans-serif}
.advantages header b{color:var(--white);font-weight:600;font-size:17px}
.advantages header em{color:var(--red);font-style:normal;font-size:22px}
.advantages .lead{font-weight:700;font-size:12.5px;color:var(--ink);line-height:1.55;padding:14px 12px 6px}
.advantages ul{list-style:none;padding:0 12px}
.advantages li{font-size:12.5px;line-height:25px;padding-left:14px;position:relative}
.advantages li::before{content:"";position:absolute;left:0;top:10px;width:6px;height:6px;border-radius:50%;background:var(--red)}

/* featured */
.featured{height:585px}
.featured h2{padding-top:8px;margin-bottom:30px}
.product-row{display:flex;gap:24px;position:relative}
.product{width:317px;height:380px;position:relative}
.product .photo{position:absolute;inset:0;background:linear-gradient(180deg,#e4e4e4,#cfcfcf)}
.product.dark{border:10px solid #e9e9e9}
.product.dark .photo{background:linear-gradient(180deg,#3a3a3a,#1f1f1f)}
.product .overlay{position:absolute;left:0;right:0;top:158px;text-align:center;color:var(--white)}
.product .dot{width:40px;height:40px;border-radius:50%;background:var(--red);margin:0 auto 36px}
.product .overlay h3{font-family:"Jost",sans-serif;font-weight:500;font-size:16px;margin-bottom:10px}
.product .overlay p{font-size:13px;line-height:1.55;padding:0 40px;color:#ddd}
.slide-btn{position:absolute;top:170px;width:34px;height:34px;border-radius:50%;background:#9a9a9a;display:flex;align-items:center;justify-content:center;z-index:2}
.slide-btn.prev{left:-16px}.slide-btn.next{right:-16px}
.center{text-align:center}
.featured .center{margin-top:36px}

/* help */
.help{height:250px;background:var(--band);text-align:center;padding-top:40px}
.help p{font-size:23px;color:var(--ink);line-height:1.45;margin:14px auto 20px;width:900px}

/* blog */
.blog{height:700px;padding-top:56px}
.blog h2{margin-bottom:38px}
.post-row{display:flex;gap:13px}
.post{width:325px;height:440px;border:1px solid #e2e2e2;padding:7px}
.post .photo{height:226px}
.post .tag{display:inline-block;margin:14px 0 12px;font-size:11px;font-weight:700;color:var(--white);padding:6px 10px;text-transform:uppercase}
.post h3{font-weight:700;font-size:17px;color:var(--ink);margin-bottom:10px}
.post .by{font-size:12px;color:var(--text);margin-bottom:12px}
.post p{font-size:12px;line-height:1.65;color:var(--text)}
.blog .center{margin-top:36px}

/* clients */
.clients{height:236px;background:var(--band);padding-top:36px}
.clients h2{margin-bottom:32px}
.client-row{display:flex;gap:15px;position:relative}
.client{width:130px;height:62px;background:var(--white);border:1px solid #ddd;display:flex;align-items:center;justify-content:center;gap:8px;font-size:19px;color:#111;font-weight:700}
.client i{width:14px;height:14px;border-radius:50%;background:#111;display:block}
.clients .chev{position:absolute;top:14px}
.clients .chev.prev{left:-44px}.clients .chev.next{right:-44px}

/* callback */
.callback{height:492px;position:relative}
.callback .visual{position:absolute;left:0;top:0;width:500px;height:492px;background:linear-gradient(90deg,#d9dadc 0%,#eeeeee 60%,#ffffff 100%)}
.callback-form{position:absolute;left:506px;top:60px;width:601px}
.callback-form h2{font-family:"Jost",sans-serif;font-weight:400;font-size:36px;color:var(--ink);margin-bottom:26px}
.field-row{display:flex;justify-content:space-between;margin-bottom:22px}
.field{width:300px;border-bottom:1px solid var(--line);font-size:13px;color:var(--text);padding-bottom:12px}
.area-label{font-size:13px;color:var(--text);margin-bottom:12px}
.area{height:90px;border:1px solid var(--line);margin-bottom:20px}
.submit{display:inline-block;background:var(--red);color:var(--white);font-weight:700;font-size:16px;padding:9px 26px}

/* footer */
.site-footer{height:60px;background:var(--charcoal)}
.site-footer .wrap{display:flex;justify-content:space-between;align-items:center;height:60px}
.site-footer small{font-size:13px;color:#ddd}
.social{display:flex;gap:8px}
.social span{width:34px;height:34px;border-radius:50%;background:#e6e6e6;display:block}
</style>
</head>
<body>

<header class="site-header">
  <div class="wrap">
    <div class="brand"><span class="mark"></span>Corvan Traders</div>
    <div class="contact">
      <span><svg width="20" height="20" viewBox="0 0 20 20"><circle cx="10" cy="10" r="9" fill="none" stroke="#ec1f27" stroke-width="1.6"/><path d="M7 5.5l2 2-1 1.5c.7 1.4 1.6 2.3 3 3l1.5-1 2 2-1.3 1.5C9.5 14.5 5.5 10.5 5.5 6.8z" fill="#ec1f27"/></svg>555.010.2244</span>
      <span><svg width="26" height="20" viewBox="0 0 26 20"><rect x="1" y="2" width="24" height="16" fill="none" stroke="#ec1f27" stroke-width="1.6"/><path d="M1 2l12 9 12-9" fill="none" stroke="#ec1f27" stroke-width="1.6"/></svg>inquiry@corvantraders.com</span>
    </div>
  </div>
</header>

<nav class="main-nav">
  <a class="active" style="left:129px">Home</a>
  <a style="left:230px">Products ▾</a>
  <a style="left:368px">Solutions ▾</a>
  <a style="left:502px">Support</a>
  <a style="left:615px">Free Trial</a>
  <a style="left:737px">About</a>
  <a style="left:838px">Login</a>
</nav>

<section class="hero" role="img" aria-label="Cargo plane over a container port with a ship at sunset">
  <span class="arrow prev"><svg width="10" height="12"><path d="M8 1L2 6l6 5z" fill="#fff"/></svg></span>
  <span class="arrow next"><svg width="10" height="12"><path d="M2 1l6 5-6 5z" fill="#fff"/></svg></span>
  <div class="hero-caption">Lorem Ipsum Dolor Sit Amet, Consectetuer Adipiscing Elit, Sed Diam</div>
</section>

<section class="intro">
  <div class="wrap">
    <div class="intro-text">
      <h1>A World with Many Screens ...</h1>
      <p class="lead">Lorem ipsum dolor sit amet, consectetuer adipiscing elit, sed diam nonummy nibh euismod tincidunt ut laoreet dolore magna aliquam erat volutpat.</p>
      <p>Lorem ipsum dolor sit amet, consectetuer adipiscing elit, sed diam nonummy nibh euismod tincidunt ut laoreet dolore magna aliquam erat volutpat. Ut wisi enim ad minim veniam, quis nostrud exerci tation ullamcorper suscipit lobortis nisl ut aliquip ex ea commodo consequat. Duis autem vel eum iriure dolor in hendrerit in vulputate velit esse molestie consequat, vel illum dolore eu feugiat nulla facilisis at vero eros et accumsan et iusto odio dignissim qui blandit praesent luptatum zzril delenit augue duis dolore.</p>
    </div>
    <aside class="advantages">
      <header><b>Corvan</b><em>Advantages</em></header>
      <p class="lead">Lorem ipsum dolor sit amet, consectetuer adipiscing elit, sed diam nonummy nibh euismod.</p>
      <ul>
        <li>Aadipiscing elit, sed diam nonummy nibh</li>
        <li>Aadipiscing elit, sed dia</li>
        <li>Aadipiscing elit, sed diam nonummy</li>
        <li>Aadipiscing elit, sed diam nonummy nibh</li>
        <li>Aadipiscing elit, sed diam no</li>
        <li>Aadipiscing elit, sed diam nonummy</li>
      </ul>
    </aside>
  </div>
</section>

<section class="featured">
  <div class="wrap">
    <h2 class="section-title">Featured Products</h2>
    <div class="product-row">
      <span class="slide-btn prev"><svg width="10" height="12"><path d="M8 1L2 6l6 5z" fill="#fff"/></svg></span>
      <div class="product"><div class="photo" role="img" aria-label="Man in a striped dress shirt and tie"></div></div>
      <div class="product dark">
        <div class="photo" role="img" aria-label="Woman in a dark lace dress"></div>
        <div class="overlay">
          <div class="dot"></div>
          <h3>Style Women Dress</h3>
          <p>Duis autem vel eum iriure dolor in hendrerit in vulputate velit.</p>
        </div>
      </div>
      <div class="product"><div class="photo" role="img" aria-label="Man in a black hooded sweatshirt"></div></div>
      <span class="slide-btn next"><svg width="10" height="12"><path d="M2 1l6 5-6 5z" fill="#fff"/></svg></span>
    </div>
    <div class="center"><span class="btn">View All</span></div>
  </div>
</section>

<section class="help">
  <h2 class="section-title">We Are Here To Help You</h2>
  <p>Lorem ipsum dolor sit amet, consectetuer adipiscing elit, sed diam nonummy nibh euismod tincidunt ut laoreet</p>
  <span class="btn">Get A Free Trail</span>
</section>

<section class="blog">
  <div class="wrap">
    <h2 class="section-title">Recent News and Blog</h2>
    <div class="post-row">
      <article class="post">
        <div class="photo" role="img" aria-label="Hands working with a calculator over financial papers" style="background:linear-gradient(135deg,#9aa3ab,#e6e8ea)"></div>
        <span class="tag" style="background:var(--red)">Lorem ipsumso</span>
        <h3>Lorem ipsum dolor consectetue</h3>
        <p class="by">By: Simply Dummy Text</p>
        <p>Lorem ipsum dolor sit amete, consectetuer adipiscing elit, sed diam nonummy nibh euismod tincidunt utlaor dolore ma aliquam erat volutpat...[+]</p>
      </article>
      <article class="post">
        <div class="photo" role="img" aria-label="Person working at a desktop computer in an office" style="background:linear-gradient(135deg,#6b5a4c,#c8c3bb)"></div>
        <span class="tag" style="background:var(--charcoal)">Lorem ips</span>
        <h3>Lorem ipsum dolor consectetuer</h3>
        <p class="by">By: Simply Dummy Text</p>
        <p>Lorem ipsum dolor sit amete, consectetuer adipiscing elit, sed diam nonummy nibh euismod tincidunt utlaor dolore ma aliquam erat volutpat...[+]</p>
      </article>
      <article class="post">
        <div class="photo" role="img" aria-label="Paper fortune teller on a sandy beach" style="background:linear-gradient(180deg,#b9c7d2,#d8cbb4)"></div>
        <span class="tag" style="background:var(--charcoal)">Lorem ipsumsd</span>
        <h3>Lorem ipsum dolor consectetuer</h3>
        <p class="by">By: Simply Dummy Text</p>
        <p>Lorem ipsum dolor sit amete, consectetuer adipiscing elit, sed diam nonummy nibh euismod tincidunt utlaor dolore ma aliquam erat volutpat...[+]</p>
      </article>
    </div>
    <div class="center"><span class="btn">View All</span></div>
  </div>
</section>

<section class="clients">
  <div class="wrap">
    <h2 class="section-title">Our Clients</h2>
    <div class="client-row">
      <svg class="chev prev" width="20" height="34" viewBox="0 0 20 34"><path d="M16 2L4 17l12 15" fill="none" stroke="#bbb" stroke-width="2"/></svg>
      <div class="client"><i></i>Nexora</div>
      <div class="client"><i></i>Halbrook</div>
      <div class="client">Quillon</div>
      <div class="client">Vantix</div>
      <div class="client"><i></i>Nexora</div>
      <div class="client">Brightmoor</div>
      <div class="client"><i></i>Halbrook</div>
      <svg class="chev next" width="20" height="34" viewBox="0 0 20 34"><path d="M4 2l12 15L4 32" fill="none" stroke="#bbb" stroke-width="2"/></svg>
    </div>
  </div>
</section>

<section class="callback">
  <div class="visual" role="img" aria-label="Laptop on a white desk with a coffee cup and a small plant"></div>
  <form class="callback-form">
    <h2>REQUEST A CALL BACK</h2>
    <div class="field-row"><div class="field">First Name</div><div class="field">Last Name</div></div>
    <div class="field-row"><div class="field">Email</div><div class="field">Phone Number</div></div>
    <p class="area-label">Details About Your Enquiry</p>
    <div class="area"></div>
    <span class="submit">SUBMIT</span>
  </form>
</section>

<footer class="site-footer">
  <div class="wrap">
    <small>Copyright © 2018 Corvan Traders. All Rights Reserved.</small>
    <div class="social">
      <span aria-label="Social link one"></span>
      <span aria-label="Social link two"></span>
      <span aria-label="Social link three"></span>
      <span aria-label="Social link four"></span>
      <span aria-label="Social link five"></span>
    </div>
  </div>
</footer>

</body>
</html>
```